International professional tennis coach needs a book cover design

This is my 2nd published book, the first one was a #1 on the best seller. I'm looking for a world class book cover design for this new book. The name of my first book was 5 Baseline Habits to Unlock Your Rally Rhythm, located on Brimlow.com

The title of the new book:

Title: The Craft of Steady Rallies
Subtitle: Building a Tactical Margin by Way of Opponent Insight

I'm uploading our new CRAFT OF STEADY logo that I'd like for you to use as the centerpiece of the book design along with a 21st century design feel that incorporates what the book topic is below::

--> This book is about building competitive intelligence by using tennis data analytics to develop and expand a player's strategic advantage for match play. <--

The colors we would like to use are Blue, Yellow, and Green. These shades of these colors should be bold! (You will see the bold color examples of blues, yellows, and greens that I'm talking about in the logos that are attached here, especially the colors for my Tennis GridRally App logo.

I will upload the Tennis GridRally logo which should go somewhere on the back cover design (small size maybe in the bottom corner).

This book is revolutionary to the standard way of teaching tennis, it is based on a decade of recording and gathering tennis data analytics and then we created on-court practice games to develop better decision making in players for the competitive edge.

My websites are www.elevatedrillzone.com and www.craftofsteadyrallies.com

```html
<!DOCTYPE html>
<html lang="en">
<head>
<meta charset="utf-8">
<title>The Craft of Steady Rallies – Book Cover</title>
<link rel="stylesheet" href="https://fonts.googleapis.com/css2?family=Lato:wght@300;400;700;900&family=Oswald:wght@600&family=Montserrat:wght@700&display=swap">
<style>
  :root {
    --paper: #ffffff;
    --stage: #43517e;
    --ink: #1f1f1f;
    --brand-blue: #2a62b0;
    --sky-top: #2468b8;
    --sky-mid: #3a9edb;
    --court-dark: #143b5e;
    --court-mid: #1c5f96;
    --gold: #f7c21a;
    --trim: #f2a7ab;
    --frame: #111111;
    --spine-guide: #3b4fb0;
  }
  * { box-sizing: border-box; margin: 0; padding: 0; }
  html, body { width: 853px; height: 1200px; overflow: hidden; background: var(--paper); }
  body { position: relative; font-family: "Lato", Arial, sans-serif; color: var(--ink); }

  /* ---------- print spread ---------- */
  .spread { position: absolute; left: 82px; top: 52px; width: 700px; height: 501px; border: 1px solid var(--trim); }
  .back-frame { position: absolute; left: 6px; top: 6px; width: 362px; height: 488px; border: 1px solid var(--frame); border-right: none; }
  .spine-guide { position: absolute; top: 0; bottom: 0; border-left: 1px dashed var(--spine-guide); }
  .spine-guide.left { left: 331px; }
  .spine-guide.right { left: 367px; }

  .back-copy { position: absolute; left: 35px; top: 38px; width: 272px; font-size: 6.9px; line-height: 8.8px; text-align: justify; hyphens: auto; }
  .back-copy p { text-indent: 8px; margin-bottom: 3.2px; }

  .author-band { position: absolute; left: 7px; top: 233px; width: 324px; height: 181px;
    background: linear-gradient(110deg, #2c8fd6 0%, #3aa6e2 25%, #1f64b6 70%, #1c5aa8 100%); }
  .author-photo { position: absolute; left: 33px; width: 67px; height: 67px; background: linear-gradient(160deg, #7a8c9c, #3d4f62 60%, #2b3440); }
  .author-photo.first { top: 9px; }
  .author-photo.second { top: 106px; background: linear-gradient(170deg, #9fb7c6, #4d6a52 55%, #2e3a48); }
  .author-bio { position: absolute; left: 108px; width: 189px; font-size: 6.3px; line-height: 8.6px; color: #fff; text-align: justify; text-indent: 8px; }
  .author-bio.first { top: 8px; }
  .author-bio.second { top: 104px; }
  .author-bio b { font-weight: 700; }

  .back-brands { position: absolute; left: 35px; top: 440px; display: flex; align-items: center; gap: 18px; }
  .brand-mark { display: flex; align-items: center; gap: 4px; font-family: "Lato", Arial, sans-serif; font-weight: 900; font-size: 8px; color: var(--brand-blue); }
  .brand-mark .dot { width: 10px; height: 10px; border-radius: 50%; background: var(--gold); }
  .brand-mark.green .dot { background: #8cc63f; }

  .spine-brand { position: absolute; left: 341px; top: 24px; width: 14px; height: 14px; border-radius: 50%; background: var(--gold); }
  .spine-title { position: absolute; left: 340px; top: 64px; writing-mode: vertical-rl; font-family: "Montserrat", Arial, sans-serif; font-weight: 700; font-size: 9.5px; letter-spacing: 0.3px; color: var(--brand-blue); }

  /* ---------- front cover component ---------- */
  .front { position: absolute; width: 332px; height: 494px; background: var(--paper); overflow: hidden; }
  .spread .front { left: 367px; top: 0; }
  .front .sky { position: absolute; left: 0; top: 0; width: 100%; height: 194px;
    background: radial-gradient(ellipse 75% 60% at 40% 70%, var(--sky-mid), transparent 80%), linear-gradient(180deg, var(--sky-top), #2d84cc); }
  .front .court { position: absolute; left: 0; top: 194px; width: 100%; height: 226px;
    background: linear-gradient(200deg, var(--court-dark) 0%, var(--court-mid) 45%, #17507f 100%); }
  .front .court-line { position: absolute; left: 0; top: 194px; }
  .front .brand-mark.cover { position: absolute; right: 20px; top: 38px; flex-direction: column; gap: 3px; font-size: 9px; color: #fff; }
  .front .brand-mark.cover .dot { width: 12px; height: 12px; }
  .front .url { position: absolute; right: 18px; top: 82px; font-size: 4px; font-weight: 700; letter-spacing: 0.2px; color: #fff; }
  .front .authors { position: absolute; left: 14px; top: 128px; font-family: "Montserrat", Arial, sans-serif; font-weight: 700; font-size: 10px; color: var(--gold); }
  .front .rule { position: absolute; left: 14px; top: 142px; width: 217px; height: 1.5px; background: #fff; }
  .front .title-top { position: absolute; left: 13px; top: 147px; font-family: "Lato", Arial, sans-serif; font-weight: 300; font-size: 37px; color: #fff; letter-spacing: 0.5px; white-space: nowrap; }
  .front .title-main { position: absolute; left: 13px; font-family: "Oswald", Arial, sans-serif; font-weight: 600; font-size: 64px; line-height: 1; letter-spacing: -1px; text-transform: uppercase; }
  .front .title-main.white { top: 190px; color: #fff; }
  .front .title-main.gold { top: 251px; color: var(--gold); }
  .front .subtitle { position: absolute; left: 15px; top: 436px; font-family: "Lato", Arial, sans-serif; font-weight: 700; font-size: 14.6px; line-height: 17.5px; color: var(--brand-blue); }

  /* ---------- presentation band ---------- */
  .stage { position: absolute; left: 0; top: 610px; width: 853px; height: 590px; background: var(--stage); }
  .stage .front { left: 293px; top: 66px; transform: scale(0.913); transform-origin: 0 0; }
</style>
</head>
<body>

<section class="spread" aria-label="Full cover spread">
  <div class="back-frame"></div>

  <div class="back-copy">
    <p>A practical guide on how to win more matches by becoming a more efficient and effective competitor.</p>
    <p>As a tennis player you have the ability to play better matches and win more of them. The Craft of Steady Rallies gives you a system to improve. We start with the individual game of the set itself. Our system examines your physical and mental progression, enabling you to upgrade your movement and performance from shot to shot and point to point. Our system seamlessly integrates the technical (physical) aspects with the tactical (mental/emotional) components, providing a comprehensive approach to elevate this performance.</p>
    <p>We aim to give you much more than how to hit great shots. Irrespective of your current skill level, we will provide you with a detailed strategic and tactical plan to enhance your performance, leading to improved results and increased success in your matches.</p>
    <p>The Craft of Steady Rallies emphasizes the importance of shifting focus from oneself to the opponent, encouraging players to analyze and understand their adversaries. By bringing the opponent back to the forefront of their thinking, the player creates the best possible context in which to improve as a competitor.</p>
    <p>In this book, we present a groundbreaking approach to tennis data analytics that seamlessly integrates match performance with practice sessions, and vice versa.</p>
  </div>

  <div class="author-band">
    <div class="author-photo first" role="img" aria-label="Portrait photo of Corwin Albrecht on court"></div>
    <p class="author-bio first"><b>CORWIN ALBRECHT</b> is regarded as one of the leading strategy and tactical coaches in the world today. He is the Creator of Tennis GridRally, the world's first Tennis Tracking App that maps and charts match play based on the rally length of a point. Corwin is a Best Selling Author of the book "5 Baseline Habits to Unlock Your Rally Rhythm" and the Co-Founder of The Craft of Steady Rallies promoting coach, player, and parent development. He is often sought after by coaches around the world to design the practice court in a way that revolutionizes a player's mindset to successfully negotiate the pressures of competitive match play.</p>
    <div class="author-photo second" role="img" aria-label="Portrait photo of Milo Danvers outdoors"></div>
    <p class="author-bio second"><b>MILO DANVERS</b> is a writer and tennis coach. He is a Co-Founder at The Craft of Steady Rallies and has been working to create a theoretical framework for tennis players of all levels to improve. Milo studies the forces that act on the player during a tennis match (both internal and external) and works with players to meet the challenge these forces represent. He runs online and on court programs designed specifically to improve a player's Competitive Intelligence.</p>
  </div>

  <div class="back-brands">
    <span class="brand-mark green"><span class="dot"></span>Tennis GridRally</span>
    <span class="brand-mark"><span class="dot"></span>Craft of Steady</span>
  </div>

  <div class="spine-guide left"></div>
  <div class="spine-guide right"></div>
  <div class="spine-brand"></div>
  <div class="spine-title">THE CRAFT OF STEADY RALLIES</div>

  <div class="front">
    <div class="sky"></div>
    <div class="court" role="img" aria-label="Photo of a blue hard court with a tennis ball beside a white line"></div>
    <svg class="court-line" width="332" height="226" viewBox="0 0 332 226" aria-hidden="true">
      <polygon points="332,75 332,112 268,226 228,226" fill="#e8e4dc" opacity="0.85"/>
    </svg>
    <div class="brand-mark cover"><span class="dot"></span>Craft of Steady</div>
    <div class="url">WWW.CRAFTOFSTEADYRALLIES.COM</div>
    <div class="authors">CORWIN ALBRECHT &amp; MILO DANVERS</div>
    <div class="rule"></div>
    <div class="title-top">THE CRAFT OF</div>
    <div class="title-main white">Steady</div>
    <div class="title-main gold">Rallies</div>
    <p class="subtitle">Building a Tactical Margin<br>by Way of Opponent Insight</p>
  </div>
</section>

<section class="stage" aria-label="Front cover presentation">
  <div class="front">
    <div class="sky"></div>
    <div class="court" role="img" aria-label="Photo of a blue hard court with a tennis ball beside a white line"></div>
    <svg class="court-line" width="332" height="226" viewBox="0 0 332 226" aria-hidden="true">
      <polygon points="332,75 332,112 268,226 228,226" fill="#e8e4dc" opacity="0.85"/>
    </svg>
    <div class="brand-mark cover"><span class="dot"></span>Craft of Steady</div>
    <div class="url">WWW.CRAFTOFSTEADYRALLIES.COM</div>
    <div class="authors">CORWIN ALBRECHT &amp; MILO DANVERS</div>
    <div class="rule"></div>
    <div class="title-top">THE CRAFT OF</div>
    <div class="title-main white">Steady</div>
    <div class="title-main gold">Rallies</div>
    <p class="subtitle">Building a Tactical Margin<br>by Way of Opponent Insight</p>
  </div>
</section>

</body>
</html>
```